Frozen Yogurt Website

I need a new website based in Sydney Pelham Wharf. Our products are:

Frozen Yogurt
Smoothies
Organic Acai Bowls / Smoothies

we have professional photos of gourmet fruit and toppings in high resolution
we have the logo
we just need a web designer

no ecommerce required. Just promotional website:

following pages are needed:

About Us
Contact Us
Frozen Yogurt
Toppings
Smoothies
Acai Bowls

examples of websites we like:
http://www.velmorastreet.com
http://myplentifulpantry.com.au/
http://www.brumo.com.au

any questions please feel free to ask
Updates

Target Market(s)

healthy and organic food lovers
Frozen yogurt / desert eaters
tourist in pelham wharf

Industry/Entity Type

Promotional

Requirements
Should not have
• no ecommerce required

```html
<!DOCTYPE html>
<html lang="en">
<head>
<meta charset="utf-8">
<title>Yovella — Frozen Yoghurt</title>
<link rel="stylesheet" href="https://fonts.googleapis.com/css2?family=Oswald:wght@400;500;600&family=Arimo:wght@400&display=swap">
<style>
  :root {
    --orange: #f26a21;
    --orange-deep: #f05a0f;
    --green: #7a9412;
    --green-light: #9bc41a;
    --green-dark: #6f9a0c;
    --charcoal: #4a4a4a;
    --slate: #515151;
    --white: #ffffff;
    --text-muted: #6e6e6e;
    --stone-light: #d2d1cf;
    --stone-mid: #c3c2bf;
    --dot: #c9c9c9;
  }
  * { box-sizing: border-box; margin: 0; padding: 0; }
  html, body {
    width: 1200px; height: 700px; overflow: hidden;
    background: var(--white);
    font-family: "Arimo", Arial, sans-serif;
  }
  .page { position: relative; width: 1200px; height: 700px; }

  .site-header { position: absolute; top: 0; left: 0; width: 1200px; height: 95px; }
  .brand {
    position: absolute; left: 122px; top: 26px;
    display: flex; align-items: center; gap: 8px;
    font-family: "Oswald", sans-serif; font-weight: 400;
    font-size: 32px; color: var(--charcoal); letter-spacing: 0.5px;
  }
  .brand-mark { width: 10px; height: 10px; border-radius: 50%; background: var(--orange); }
  .social { position: absolute; right: 122px; top: 35px; display: flex; gap: 8px; list-style: none; }
  .social li { width: 24px; height: 24px; background: var(--charcoal); }
  .social li:nth-child(odd) { background: var(--orange); }

  .hero {
    position: absolute; top: 116px; left: 0; width: 1200px; height: 480px;
    background: linear-gradient(135deg, var(--stone-light), var(--stone-mid) 60%, var(--stone-light));
  }
  .hero-photo {
    position: absolute; left: 0; top: 0; width: 760px; height: 480px;
    background: radial-gradient(ellipse at 55% 60%, rgba(240,130,90,0.35), rgba(120,140,90,0.15) 55%, transparent 75%);
  }
  .promo { position: absolute; left: 682px; top: 138px; font-family: "Oswald", sans-serif; text-transform: uppercase; }
  .promo-line { font-weight: 600; font-size: 52px; line-height: 58px; letter-spacing: -0.5px; }
  .promo-line.orange { color: var(--orange); }
  .promo-line.green { color: var(--green); }
  .promo-sub { margin-top: 10px; font-weight: 500; font-size: 25px; line-height: 36px; color: var(--slate); }
  .slider-dots { position: absolute; left: 554px; top: 403px; display: flex; gap: 8px; list-style: none; }
  .slider-dots li { width: 12px; height: 12px; border-radius: 50%; background: var(--dot); }
  .slider-dots li.active { background: #a9a9a9; }

  .main-nav {
    position: absolute; left: 120px; top: 95px; width: 960px; height: 41px;
    background: var(--charcoal); display: flex; list-style: none;
    font-family: "Oswald", sans-serif; font-size: 15px; color: var(--white);
  }
  .main-nav li { display: flex; align-items: center; justify-content: center; }
  .main-nav li.current { background: var(--orange); }

  .newsletter {
    position: absolute; left: 120px; top: 557px; width: 960px; height: 64px;
    background: var(--orange-deep); display: flex; align-items: center;
  }
  .newsletter-title {
    font-family: "Oswald", sans-serif; font-weight: 500; font-size: 27px;
    color: var(--white); text-transform: uppercase; margin-left: 24px; width: 326px;
  }
  .field {
    width: 250px; height: 34px; background: var(--white); margin-right: 10px;
    font-size: 12.5px; color: #333; display: flex; align-items: center; padding-left: 8px;
  }
  .submit {
    width: 80px; height: 34px; margin-left: -2px;
    background: linear-gradient(var(--green-light), var(--green-dark));
    color: var(--white); font-family: "Oswald", sans-serif; font-size: 16px;
    display: flex; align-items: center; justify-content: center;
  }

  .site-footer {
    position: absolute; left: 120px; top: 655px; width: 960px;
    display: flex; justify-content: space-between; font-size: 12px; color: var(--text-muted);
  }
</style>
</head>
<body>
<div class="page">
  <header class="site-header">
    <div class="brand"><span>yovella</span><span class="brand-mark"></span></div>
    <ul class="social" aria-label="Social links">
      <li></li><li></li><li></li><li></li><li></li><li></li>
    </ul>
  </header>

  <section class="hero">
    <div class="hero-photo" role="img" aria-label="Photograph of halved peaches, grapefruit, coconut cake pieces and green leaves scattered on grey concrete"></div>
    <div class="promo">
      <p class="promo-line orange">Free Frozen</p>
      <p class="promo-line green">Yoghurt + Topings!</p>
      <p class="promo-sub">Buy 1 frozem yoghurt &amp;<br>get the 2nd one free!</p>
    </div>
    <ul class="slider-dots">
      <li class="active"></li><li></li><li></li><li></li><li></li>
    </ul>
  </section>

  <ul class="main-nav">
    <li class="current" style="width:103px">HOME</li>
    <li style="width:134px">ABOUT US</li>
    <li style="width:160px">FROZEN YOGURT</li>
    <li style="width:140px">TOPPINGS</li>
    <li style="width:136px">SMOOTHIES</li>
    <li style="width:146px">ACAI BOWLS</li>
    <li style="width:141px">CONTACT US</li>
  </ul>

  <form class="newsletter">
    <h2 class="newsletter-title">Subscribe our newsletter</h2>
    <div class="field">Enter your Name</div>
    <div class="field">Enter your email</div>
    <div class="submit">SUBMIT</div>
  </form>

  <footer class="site-footer">
    <span>©2013 Yovella frozen yoghurt &nbsp;| All Rights Reserved.</span>
    <span>Terms of Service | Privacy Statement</span>
  </footer>
</div>
</body>
</html>
```